Card design for Heating and Cooling company

this is for a heating and cooling company we recently updated our logo and need to update our cards. We attached our logo so you can incorporate it into the card. We specialize in residential and commercial furnace and air condition repairs. Have been in business since 2014.

Phone number 555.284.9137

We need the following phrases
:Repairs, Installations, and maintenance
:Quality work at reasonable prices
:residential/commercial
:Licensed &Insured
:Email Pinegrovehvac47@mailbox-example.com
Name: Teodor K (Ted)
Also on back side I would like my logo with wording :Thank you for your business and refferal

Industry/Entity Type

Hvac

Contact Information for Business Card

:residential/commercial
:Licensed & Insured
Name: Teodor K (Ted)
Number:555.284.9136

Requirements
Must have
• Blue and red colors
Nice to have
• Maybe a pic of a furnace or air conditioner

```html
<!DOCTYPE html>
<html lang="en">
<head>
<meta charset="utf-8">
<title>Pinegrove Heating &amp; Cooling – Business Card</title>
<link href="https://fonts.googleapis.com/css2?family=Source+Sans+3:ital,wght@0,400;0,600;0,700;1,400&display=swap" rel="stylesheet">
<style>
  :root {
    --bg: #7a8594;
    --card-white: #ffffff;
    --card-black: #000000;
    --ink: #111111;
    --blue: #3a97f0;
    --red: #e5121b;
    --white: #ffffff;
  }
  * { box-sizing: border-box; margin: 0; padding: 0; }
  html, body { width: 1200px; height: 1024px; overflow: hidden; }
  body {
    background: var(--bg);
    font-family: "Source Sans 3", "Myriad Pro", sans-serif;
    display: flex;
    flex-direction: column;
    align-items: center;
    justify-content: center;
    gap: 40px;
  }
  .card {
    position: relative;
    width: 770px;
    height: 440px;
    box-shadow: 0 6px 18px rgba(0,0,0,.35);
  }
  .card--front { background: var(--card-white); color: var(--ink); }
  .card--back { background: var(--card-black); color: var(--white); }

  .tagline { position: absolute; font-size: 25px; color: var(--blue); }
  .tagline--services { left: 44px; top: 36px; }
  .tagline--quality { right: 44px; bottom: 40px; }

  .badge { position: absolute; font-size: 25px; color: var(--red); }
  .badge--licensed { right: 44px; top: 36px; }
  .badge--sector { left: 44px; bottom: 40px; }

  .brand {
    position: absolute;
    display: flex;
    align-items: center;
    gap: 12px;
    font-weight: 700;
    font-size: 28px;
    line-height: 1.05;
    text-transform: uppercase;
  }
  .brand__dot { width: 26px; height: 26px; border-radius: 50%; background: var(--blue); flex: none; }
  .card--front .brand { left: 44px; top: 190px; color: var(--ink); }
  .card--back .brand { left: 50%; top: 50%; transform: translate(-50%, -50%); color: var(--white); }

  .contact { position: absolute; left: 400px; top: 160px; }
  .contact__name { font-size: 30px; font-weight: 600; color: var(--blue); margin-bottom: 6px; }
  .contact__line { font-size: 23px; color: var(--ink); line-height: 1.3; }

  .thanks {
    position: absolute;
    left: 0; right: 0; bottom: 44px;
    text-align: center;
    font-size: 25px;
    font-style: italic;
  }
</style>
</head>
<body>
  <section class="card card--front" aria-label="Business card front">
    <p class="tagline tagline--services">Repairs, Installations, and Maintenance</p>
    <p class="badge badge--licensed">Licensed &amp; Insured</p>
    <div class="brand"><span class="brand__dot"></span><span>Pinegrove<br>Heating &amp; Cooling</span></div>
    <div class="contact">
      <p class="contact__name">Teodor K (Ted)</p>
      <p class="contact__line">555.284.9136</p>
      <p class="contact__line">Pinegrovehvac47@mailbox-example.com</p>
    </div>
    <p class="badge badge--sector">Residential / Commercial</p>
    <p class="tagline tagline--quality">Quality Work at Reasonable Prices</p>
  </section>

  <section class="card card--back" aria-label="Business card back">
    <div class="brand"><span class="brand__dot"></span><span>Pinegrove<br>Heating &amp; Cooling</span></div>
    <p class="thanks">Thank you for your business and refferal</p>
  </section>
</body>
</html>
```